VelnoriCore Business Cards

Will need a front and back design for a business card for VelnoriCore.
Can accept the final product as an illustrator file.
www.velnoricore-example.com is the company website.

Target Market(s)

he target market are Chief Technology Officers and people in the tech field.

Industry/Entity Type

Business

Requirements
Must have
• - The business card must have on one of the sides
name
title
company
phone
email
website
The other side may be of some design, derivation of logo and or colors

```html
<!DOCTYPE html>
<html lang="en">
<head>
<meta charset="utf-8">
<title>VelnoriCore Business Card</title>
<link href="https://fonts.googleapis.com/css2?family=Dosis:wght@500;600;700&display=swap" rel="stylesheet">
<style>
  :root {
    --page-bg: #eff2f2;
    --card-white: #ffffff;
    --brand-blue: #0a5ae8;
    --mark-blue: #1c3fc8;
    --text-light: #ffffff;
  }
  * { margin: 0; padding: 0; box-sizing: border-box; }
  html, body {
    width: 1200px;
    height: 900px;
    overflow: hidden;
    background: var(--page-bg);
    font-family: "Dosis", sans-serif;
  }
  .canvas {
    position: relative;
    width: 1200px;
    height: 900px;
  }
  .card {
    position: absolute;
    width: 618px;
    height: 353px;
  }
  .card-front {
    left: 282px;
    top: 72px;
    background: var(--card-white);
    display: flex;
    flex-direction: column;
    align-items: center;
  }
  .brand-circle {
    margin-top: 71px;
    width: 152px;
    height: 152px;
  }
  .brand-name {
    margin-top: 22px;
    font-size: 34px;
    font-weight: 700;
    letter-spacing: 0.5px;
    color: var(--mark-blue);
    line-height: 1;
  }
  .card-back {
    left: 285px;
    top: 470px;
    width: 617px;
    height: 352px;
    background: var(--brand-blue);
    color: var(--text-light);
    padding: 72px 0 0 66px;
  }
  .contact-name {
    font-size: 21px;
    font-weight: 600;
    letter-spacing: 1px;
    line-height: 26px;
  }
  .contact-title {
    font-size: 18px;
    font-weight: 500;
    letter-spacing: 1px;
    line-height: 24px;
  }
  .contact-company {
    margin-top: 24px;
    font-size: 21px;
    font-weight: 600;
    letter-spacing: 0.5px;
    line-height: 26px;
  }
  .contact-list {
    list-style: none;
    margin-top: 22px;
  }
  .contact-list li {
    font-size: 19px;
    font-weight: 500;
    letter-spacing: 1px;
    line-height: 33px;
  }
  .contact-list .phone { font-size: 20px; }
</style>
</head>
<body>
<main class="canvas">
  <section class="card card-front" aria-label="Card front">
    <svg class="brand-circle" viewBox="0 0 152 152" aria-hidden="true">
      <circle cx="76" cy="76" r="76" fill="var(--mark-blue)"/>
    </svg>
    <div class="brand-name">VelnoriCore</div>
  </section>

  <section class="card card-back" aria-label="Card back">
    <p class="contact-name">Maren Osterly</p>
    <p class="contact-title">CEO</p>
    <p class="contact-company">VelnoriCore</p>
    <ul class="contact-list">
      <li class="phone">(555)&nbsp; 013 - 4782</li>
      <li class="email">marenosterly@example.com</li>
      <li class="website">www.velnoricore-example.com</li>
    </ul>
  </section>
</main>
</body>
</html>
```